Startup photography business has a new logo, now we need business cards

Design a business card for the two partners of our business.
Our business Brisk Pelican has a new logo and we need to design a business card to showcase it and us.
Our colours of blue and orange are punchy and vivid, but how can we make the most of it on our card?

It should have our name Brisk Pelican
name of partner
phone number
email
website

Industry/Entity Type

Professional Photography

Contact Information for Business Card

Tom Ashworth
+61 400 55 61 72
tom@briskpelican.com.au
briskpelican.com.au

second card
Neil Porter
+61 400 918 263
neil@briskpelican.com.au
briskpelican.com.au

Colors
f37122
f68d4c
33a6d7
0592cd

Requirements
Must have
• one version of our logo, we have included options
• Name
• phone number
• email
• website
Nice to have
• instagram briskpelicanmedia
• twitter briskpelicanmedia
• facebook briskpelicanmedia

```html
<!DOCTYPE html>
<html lang="en">
<head>
<meta charset="utf-8">
<title>Brisk Pelican – Business Card</title>
<link rel="stylesheet" href="https://fonts.googleapis.com/css2?family=Montserrat:wght@700;800&family=Lato:wght@400&display=swap">
<style>
  :root {
    --backdrop: #e9e7e4;
    --card-white: #ffffff;
    --brand-blue: #0592cd;
    --brand-blue-light: #33a6d7;
    --brand-orange: #f37122;
    --brand-orange-light: #f68d4c;
    --card-black: #141414;
    --black-emboss: #262626;
    --text-white: #ffffff;
  }
  * { box-sizing: border-box; margin: 0; padding: 0; }
  html, body {
    width: 1200px; height: 716px; overflow: hidden;
    background: var(--backdrop);
  }
  .stage {
    position: relative; width: 1200px; height: 716px;
    display: flex; align-items: center; justify-content: center; gap: 40px;
  }
  .card {
    position: relative; width: 540px; height: 309px;
    border-radius: 4px; overflow: hidden;
  }
  /* back side */
  .card-back { background: var(--card-black); }
  .card-back .wordmark {
    position: absolute; left: 0; right: 0; top: 0; bottom: 0;
    display: flex; align-items: center; justify-content: center; gap: 14px;
  }
  .card-back .wordmark-dot {
    width: 34px; height: 34px; border-radius: 50%;
    background: var(--black-emboss);
  }
  .card-back .wordmark-name {
    font-family: "Montserrat", sans-serif; font-weight: 800;
    font-size: 34px; letter-spacing: 0.5px; color: var(--black-emboss);
  }
  /* front side */
  .card-front { background: var(--card-white); }
  .card-front .swoosh { position: absolute; inset: 0; }
  .card-front .wordmark {
    position: absolute; left: 28px; top: 132px;
    display: flex; align-items: center; gap: 10px;
  }
  .card-front .wordmark-dot {
    width: 20px; height: 20px; border-radius: 50%;
    background: var(--brand-blue);
  }
  .card-front .wordmark-name {
    font-family: "Montserrat", sans-serif; font-weight: 800;
    font-size: 24px; color: var(--brand-blue);
  }
  .contact {
    position: absolute; left: 318px; top: 116px; color: var(--text-white);
  }
  .contact-name {
    font-family: "Montserrat", sans-serif; font-weight: 700;
    font-size: 15px; letter-spacing: 0.4px; text-transform: uppercase;
    margin-bottom: 12px;
  }
  .contact-list { list-style: none; }
  .contact-list li {
    display: flex; align-items: center; gap: 10px;
    font-family: "Lato", sans-serif; font-size: 12.5px;
    line-height: 19px;
  }
  .contact-list svg { width: 10px; height: 10px; flex: none; }
</style>
</head>
<body>
<main class="stage">
  <section class="card card-back" aria-label="Card back">
    <div class="wordmark">
      <span class="wordmark-dot"></span>
      <span class="wordmark-name">Brisk Pelican</span>
    </div>
  </section>

  <section class="card card-front" aria-label="Card front">
    <svg class="swoosh" viewBox="0 0 540 309" preserveAspectRatio="none" aria-hidden="true">
      <path d="M312 0 C290 110 250 230 170 309 L540 309 L540 0 Z" fill="var(--brand-blue)"/>
      <path d="M300 0 C282 110 240 225 160 309" fill="none" stroke="var(--brand-orange)" stroke-width="5"/>
    </svg>
    <div class="wordmark">
      <span class="wordmark-dot"></span>
      <span class="wordmark-name">Brisk Pelican</span>
    </div>
    <div class="contact">
      <p class="contact-name">Tom Ashworth</p>
      <ul class="contact-list">
        <li>
          <svg viewBox="0 0 10 10"><path d="M2 1 L4 1 L4.5 3 L3.3 3.8 C4 5.3 4.7 6 6.2 6.7 L7 5.5 L9 6 L9 8 C5 8.5 1.5 5 2 1 Z" fill="#fff"/></svg>
          +61 400 55 61 72
        </li>
        <li>
          <svg viewBox="0 0 10 10"><rect x="0.5" y="2" width="9" height="6.5" fill="none" stroke="#fff"/><path d="M0.5 2 L5 5.5 L9.5 2" fill="none" stroke="#fff"/></svg>
          tom@briskpelican.com.au
        </li>
        <li>
          <svg viewBox="0 0 10 10"><circle cx="5" cy="5" r="4.3" fill="none" stroke="#fff"/><ellipse cx="5" cy="5" rx="1.8" ry="4.3" fill="none" stroke="#fff" stroke-width="0.8"/><path d="M0.7 5 H9.3" stroke="#fff" stroke-width="0.8"/></svg>
          www.briskpelican.com.au
        </li>
      </ul>
    </div>
  </section>
</main>
</body>
</html>
```